Business cards for Marrowfield Consulting with the following info for the front side:

Marrowfield Consulting
Executive Coaching and Human Capital Strategy
www.marrowfield.example

Idalia Renvoort
Principal
idalia@marrowfield.example
+1 555 274 9186

Black background, text using the colours of the logo - enclosed.

The back side of the business card should feature the logo in the middle, with "Executive Coaching and Human Capital Strategy" on top and "www.marrowfield.example" below.

```html
<!DOCTYPE html>
<html lang="en">
<head>
<meta charset="utf-8">
<title>Marrowfield Consulting — Business Cards</title>
<link rel="stylesheet" href="https://fonts.googleapis.com/css2?family=Montserrat:wght@400;500;600;700&display=swap">
<style>
  :root {
    --backdrop: #3b3b3c;
    --card: #1f1f20;
    --brand-blue: #30a5d8;
    --brand-yellow: #f7bd17;
    --ink-light: #f2f2f2;
    --ink-muted: #c9c9c9;
    --ink-dark: #1f1f20;
    --divider: #4a4a4a;
  }
  * { margin: 0; padding: 0; box-sizing: border-box; }
  html, body {
    width: 1200px; height: 1015px; overflow: hidden;
    background: var(--backdrop);
    font-family: "Montserrat", Arial, sans-serif;
  }
  .canvas { position: relative; width: 1200px; height: 1015px; }

  .card {
    position: absolute; left: 230px; width: 740px; height: 423px;
    background: var(--card); overflow: hidden;
    box-shadow: 0 14px 30px rgba(0,0,0,.45);
  }
  .card--back { top: 60px; }
  .card--front { top: 532px; }

  /* Back side */
  .accent-line { position: absolute; height: 7px; background: var(--brand-blue); }
  .accent-line--top { top: 40px; right: 0; width: 300px; }
  .accent-line--left { top: 128px; left: 0; width: 180px; }

  .tagline {
    position: absolute; left: 200px; top: 100px; width: 260px;
    color: var(--ink-muted); font-size: 15px; line-height: 17px;
    text-transform: uppercase; letter-spacing: .2px;
  }
  .brand {
    position: absolute; display: flex; align-items: center; gap: 14px;
  }
  .card--back .brand { left: 190px; top: 172px; }
  .brand__dot {
    width: 52px; height: 52px; border-radius: 50%;
    border: 3px solid var(--brand-yellow); flex: none;
  }
  .brand__name {
    color: var(--brand-blue); font-weight: 600; font-size: 40px;
    letter-spacing: 1px; text-transform: uppercase;
  }

  .band {
    position: absolute; left: 0; right: 0; bottom: 0; height: 108px;
    display: flex; align-items: center; justify-content: center;
    font-size: 20px; font-weight: 500; letter-spacing: .5px; text-transform: uppercase;
  }
  .band--yellow { background: var(--brand-yellow); color: var(--ink-dark); }
  .band--blue { background: var(--brand-blue); color: #ffffff; height: 112px; }

  /* Front side */
  .card--front .brand {
    left: 40px; top: 88px; width: 330px;
    flex-direction: column; gap: 16px;
  }
  .card--front .brand__dot { width: 64px; height: 64px; }
  .card--front .brand__name { font-size: 34px; }

  .divider {
    position: absolute; left: 390px; top: 60px; width: 1px; height: 170px;
    background: var(--divider);
  }
  .contact { position: absolute; left: 420px; top: 66px; }
  .contact__name {
    color: var(--brand-blue); font-weight: 700; font-size: 24px;
    text-transform: uppercase; letter-spacing: .5px;
  }
  .contact__role { color: var(--ink-light); font-size: 17px; margin-top: 2px; }
  .contact__list { list-style: none; margin-top: 30px; }
  .contact__item {
    display: flex; align-items: center; gap: 12px;
    color: var(--ink-light); font-size: 16px; line-height: 26px;
  }
  .contact__icon { width: 20px; height: 18px; flex: none; }
</style>
</head>
<body>
<main class="canvas">

  <section class="card card--back" aria-label="Card back">
    <span class="accent-line accent-line--top"></span>
    <p class="tagline">Executive Coaching and<br>Human Capital Strategy</p>
    <span class="accent-line accent-line--left"></span>
    <div class="brand">
      <span class="brand__dot"></span>
      <span class="brand__name">Marrowfield</span>
    </div>
    <div class="band band--yellow">www.marrowfield.example</div>
  </section>

  <section class="card card--front" aria-label="Card front">
    <div class="brand">
      <span class="brand__dot"></span>
      <span class="brand__name">Marrowfield</span>
    </div>
    <span class="divider"></span>
    <div class="contact">
      <h1 class="contact__name">Idalia Renvoort</h1>
      <p class="contact__role">Principal</p>
      <ul class="contact__list">
        <li class="contact__item">
          <svg class="contact__icon" viewBox="0 0 20 18" aria-hidden="true">
            <rect x="1" y="1" width="18" height="16" rx="2" fill="none" stroke="#30a5d8" stroke-width="1.6"/>
            <path d="M6 4.5c-.8.8-.6 3 1.6 5.4s4.6 3 5.6 2.2l.9-1-2-1.6-1 .8c-.8-.3-2.3-1.8-2.6-2.6l.8-1-1.5-2.1z" fill="#30a5d8"/>
          </svg>
          +1 555 274 9186
        </li>
        <li class="contact__item">
          <svg class="contact__icon" viewBox="0 0 20 18" aria-hidden="true">
            <rect x="1" y="3" width="18" height="12" fill="none" stroke="#30a5d8" stroke-width="1.6"/>
            <path d="M1 3l9 7 9-7M1 15l7-6M19 15l-7-6" fill="none" stroke="#30a5d8" stroke-width="1.6"/>
          </svg>
          idalia@marrowfield.example
        </li>
      </ul>
    </div>
    <div class="band band--blue">www.marrowfield.example</div>
  </section>

</main>
</body>
</html>
```